Business Card Re-Design

Consulting Company: To build a high performance organization, you need great leaders at all levels throughout your organization. The Northvale Talent Growth Studio engages, inspires, and educates current and future leaders to step beyond the ordinary and deliver exceptional results. This new breed of leaders will motivate your staff to leave the safety of complacency behind and come together to build an extraordinary organization. The current trend has been to ask our people to do more with fewer resources. People have been stepping up to the challenge, but more is required to ensure success with a new work paradigm. We work with your management team to build a successful strategy that will make your organization more effective. NTGS then supports your management team by providing a comprehensive set of proven services to empower your entire organization to successfully execute new strategies.Let NTGS help you optimize your organization’s individual and team performance today!

Target Market(s)

Federal, State and Local Government / Non profit

Industry/Entity Type

Management Consulting

Contact Information for Business Card

NTGS, inc (Northvale Talent Growth Studio) Building Stronger Leaders and High-Performing Teams

Colors
fee18a
ec1f27
474747
fbf289

Requirements
Must have
• Professional and high quality feel

```html
<!DOCTYPE html>
<html lang="en">
<head>
<meta charset="utf-8">
<title>Northvale Talent Growth Studio – Business Card</title>
<link rel="stylesheet" href="https://fonts.googleapis.com/css2?family=PT+Sans:ital,wght@0,400;0,700;1,400&display=swap">
<style>
  :root {
    --page-bg: #ffffff;
    --card-bg: #ffffff;
    --card-edge: #9a9a9a;
    --brand-ink: #5a5444;
    --tagline-ink: #6b6650;
    --accent-red: #b5262c;
    --body-ink: #474747;
  }
  * { margin: 0; padding: 0; box-sizing: border-box; }
  html, body {
    width: 1200px;
    height: 900px;
    overflow: hidden;
    background: var(--page-bg);
  }
  .canvas {
    position: relative;
    width: 1200px;
    height: 900px;
  }
  .business-card {
    position: absolute;
    left: 371px;
    top: 60px;
    width: 458px;
    height: 780px;
    background: var(--card-bg);
    border: 1px solid var(--card-edge);
    font-family: "PT Sans", sans-serif;
    text-align: center;
  }
  .brand-mark {
    position: absolute;
    left: 50%;
    top: 70px;
    transform: translateX(-50%);
    width: 90px;
    height: 90px;
    display: block;
  }
  .brand-name {
    position: absolute;
    left: 0;
    right: 0;
    top: 184px;
    font-size: 27px;
    line-height: 32px;
    font-weight: 700;
    color: var(--brand-ink);
    white-space: nowrap;
  }
  .brand-tagline {
    position: absolute;
    left: 0;
    right: 0;
    top: 246px;
    font-size: 16px;
    line-height: 20px;
    font-style: italic;
    color: var(--tagline-ink);
    white-space: nowrap;
  }
  .holder {
    position: absolute;
    left: 0;
    right: 0;
    top: 356px;
    color: var(--accent-red);
    font-weight: 700;
    font-size: 32px;
    line-height: 40px;
    text-transform: uppercase;
  }
  .contact {
    position: absolute;
    left: 0;
    right: 0;
    top: 588px;
    color: var(--body-ink);
    font-size: 23px;
    line-height: 29px;
    font-style: normal;
  }
</style>
</head>
<body>
  <main class="canvas">
    <section class="business-card" aria-label="Business card front">
      <svg class="brand-mark" viewBox="0 0 90 90" aria-hidden="true">
        <circle cx="45" cy="45" r="38" fill="var(--brand-ink)"/>
      </svg>
      <h1 class="brand-name">Northvale Talent Growth Studio</h1>
      <p class="brand-tagline">Building Stronger Leaders and High-Performing Teams</p>
      <div class="holder">
        <p class="holder-name">Marcus L. Whitfield</p>
        <p class="holder-title">President / CEO</p>
      </div>
      <address class="contact">
        <span class="contact-street">4270 Larkspur Commons</span><br>
        <span class="contact-city">Glenhaven, MD 20916</span><br>
        <span class="contact-phone">301.555.0148</span><br>
        <span class="contact-fax">FAX: 301.555.0173</span>
      </address>
    </section>
  </main>
</body>
</html>
```